Business card design needed

Our modern electrical contracting company requires business card design utilising our logo and incorporating our tag line "Service when you need it". We specialise in assisting our customers 24/7 offering a breakdown service.

Industry/Entity Type

Electrical

Contact Information for Business Card

Marcus Penhale, Electrical contractor,Tel: (08) 8456 3071, Fax: (08) 8679 4315, Mob 0438 562 740, Email: marcus.penhale@brightwirepower.com.au, Web: www.brightwirepower.com.au

Requirements
Must have
• we require a 2 sided card.
Front- Logo, tag line and contact information.
Rear- service when you need it! Call now for our 24/7 breakdown service

```html
<!DOCTYPE html>
<html lang="en">
<head>
<meta charset="utf-8">
<title>Service when you need it – rear of card</title>
<link rel="stylesheet" href="https://fonts.googleapis.com/css2?family=Gelasio:ital,wght@0,600;1,400&display=swap">
<style>
  :root {
    --card-bg: #d6ddee;
    --card-bg-deep: #cdd5ea;
    --emblem-fill: #c8d2e8;
    --headline-top: #4470b5;
    --headline-bottom: #1f4586;
    --subline: #333338;
  }
  * { margin: 0; padding: 0; box-sizing: border-box; }
  html, body {
    width: 1200px;
    height: 741px;
    overflow: hidden;
  }
  body {
    background: var(--card-bg);
  }
  .card-rear {
    position: relative;
    width: 1200px;
    height: 741px;
    overflow: hidden;
    background: radial-gradient(ellipse at 50% 50%, var(--card-bg) 0%, var(--card-bg) 55%, var(--card-bg-deep) 100%);
  }
  .emblem-backdrop {
    position: absolute;
    left: 0;
    top: 0;
    width: 1200px;
    height: 741px;
  }
  .tagline {
    position: absolute;
    right: 63px;
    top: 303px;
    font-family: "Gelasio", "Century Schoolbook", serif;
    font-weight: 600;
    font-size: 83px;
    line-height: 1;
    letter-spacing: 0.4px;
    white-space: nowrap;
    background: linear-gradient(to bottom, var(--headline-top), var(--headline-bottom));
    -webkit-background-clip: text;
    background-clip: text;
    color: transparent;
  }
  .call-to-action {
    position: absolute;
    right: 74px;
    top: 418px;
    font-family: "Gelasio", "Century Schoolbook", serif;
    font-style: italic;
    font-weight: 400;
    font-size: 34px;
    line-height: 1;
    color: var(--subline);
    white-space: nowrap;
  }
</style>
</head>
<body>
  <main class="card-rear">
    <svg class="emblem-backdrop" viewBox="0 0 1200 741" aria-hidden="true">
      <circle cx="632" cy="373" r="344" fill="var(--emblem-fill)" opacity="0.7"/>
    </svg>
    <h1 class="tagline">service when you need it!</h1>
    <p class="call-to-action">Call now for our 24/7 breakdown service</p>
  </main>
</body>
</html>
```